Urine collection cup with and without sterile seal sticker

Hello. We need a urine cup label designed please with

Name:
Date of Birth:
Date:
Time:
Temp℃:
Specimen ID:

Product code: KTX-58
Volume markings (e.g., 30 mL, 60 mL, 90 mL).
Vesk Lab Checks logo

Could you please provide one version with the additional sterile sticker extending to the top, and one version without the additional sterile sticker?

```html
<!DOCTYPE html>
<html lang="en">
<head>
<meta charset="utf-8">
<title>KTX-58 Urine Cup Labels</title>
<link href="https://fonts.googleapis.com/css2?family=Inter:wght@600;700&family=Poppins:wght@500;600;700;800&display=swap" rel="stylesheet">
<style>
  :root {
    --backdrop: #909396;
    --label: #ffffff;
    --field: #e8f0f6;
    --ink: #1b2430;
    --brand: #2a9fe0;
    --brand-dark: #1b3a5c;
    --seal-top: #31b2e6;
    --seal-bottom: #1d4c86;
  }
  * { margin: 0; padding: 0; box-sizing: border-box; }
  html, body { width: 1200px; height: 749px; overflow: hidden; background: var(--backdrop); }
  .canvas { position: relative; width: 1200px; height: 749px; }

  .label {
    position: absolute;
    top: 236px;
    width: 465px;
    height: 413px;
    background: var(--label);
    box-shadow: 0 10px 14px rgba(0,0,0,0.22);
    font-family: "Inter", sans-serif;
    color: var(--ink);
  }
  .label--plain { left: 54px; border-radius: 36px; }
  .label--sealed { left: 600px; border-radius: 36px 0 0 36px; }

  .field-name {
    position: absolute;
    font-weight: 700;
    font-size: 16px;
    line-height: 20px;
  }
  .field-box {
    position: absolute;
    height: 40px;
    background: var(--field);
    border-radius: 6px;
  }

  .brand {
    position: absolute;
    left: 28px;
    top: 355px;
    display: flex;
    align-items: center;
    gap: 6px;
  }
  .brand-dot {
    width: 32px; height: 32px; border-radius: 50%;
    background: var(--brand);
  }
  .brand-name {
    font-family: "Poppins", sans-serif;
    font-weight: 700;
    font-size: 20px;
    color: var(--brand-dark);
  }

  .product {
    position: absolute;
    right: 42px;
    top: 338px;
    text-align: right;
    font-family: "Poppins", sans-serif;
  }
  .product-code {
    font-weight: 700;
    font-size: 28px;
    line-height: 34px;
    color: var(--brand);
    letter-spacing: 0.5px;
  }
  .product-volume {
    font-weight: 500;
    font-size: 13px;
    line-height: 16px;
    color: var(--ink);
  }

  .seal {
    position: absolute;
    left: 1065px;
    top: 41px;
    width: 81px;
    height: 608px;
    border-radius: 24px 24px 24px 0;
    background: linear-gradient(180deg, var(--seal-top), var(--seal-bottom));
    box-shadow: 0 10px 14px rgba(0,0,0,0.22);
    color: #ffffff;
    font-family: "Poppins", sans-serif;
  }
  .seal-title {
    position: absolute;
    left: 8px;
    top: 70px;
    writing-mode: vertical-rl;
    font-weight: 800;
    font-size: 60px;
    line-height: 64px;
    letter-spacing: 0.5px;
  }
  .seal-note {
    position: absolute;
    left: 12px;
    top: 429px;
    writing-mode: vertical-rl;
    font-weight: 700;
    font-size: 16px;
    line-height: 21px;
  }
</style>
</head>
<body>
<div class="canvas">

  <section class="label label--plain">
    <span class="field-name" style="left:28px;top:44px">Name:</span>
    <span class="field-box" style="left:90px;top:34px;width:346px"></span>
    <span class="field-name" style="left:28px;top:104px">Date of Birth:</span>
    <span class="field-box" style="left:145px;top:95px;width:291px"></span>
    <span class="field-name" style="left:28px;top:166px">Date:</span>
    <span class="field-box" style="left:80px;top:157px;width:168px"></span>
    <span class="field-name" style="left:257px;top:166px">Time:</span>
    <span class="field-box" style="left:315px;top:158px;width:121px"></span>
    <span class="field-name" style="left:28px;top:226px">Temp°C:</span>
    <span class="field-box" style="left:110px;top:215px;width:326px"></span>
    <span class="field-name" style="left:28px;top:286px">Specimen ID:</span>
    <span class="field-box" style="left:145px;top:274px;width:291px"></span>
    <div class="brand"><span class="brand-dot"></span><span class="brand-name">Vesk Lab Checks</span></div>
    <div class="product"><div class="product-code">KTX-58</div><div class="product-volume">30 mL</div></div>
  </section>

  <section class="label label--sealed">
    <span class="field-name" style="left:28px;top:44px">Name:</span>
    <span class="field-box" style="left:89px;top:37px;width:346px"></span>
    <span class="field-name" style="left:28px;top:104px">Date of Birth:</span>
    <span class="field-box" style="left:143px;top:98px;width:292px"></span>
    <span class="field-name" style="left:28px;top:166px">Date:</span>
    <span class="field-box" style="left:79px;top:160px;width:168px"></span>
    <span class="field-name" style="left:257px;top:166px">Time:</span>
    <span class="field-box" style="left:314px;top:161px;width:121px"></span>
    <span class="field-name" style="left:28px;top:226px">Temp°C:</span>
    <span class="field-box" style="left:109px;top:218px;width:326px"></span>
    <span class="field-name" style="left:28px;top:286px">Specimen ID:</span>
    <span class="field-box" style="left:143px;top:277px;width:292px"></span>
    <div class="brand"><span class="brand-dot"></span><span class="brand-name">Vesk Lab Checks</span></div>
    <div class="product" style="top:343px"><div class="product-code">KTX-58</div><div class="product-volume">30 mL</div></div>
  </section>

  <aside class="seal">
    <div class="seal-title">Nonsterile</div>
    <div class="seal-note">Interior<br>As long as seal<br>remains intact</div>
  </aside>

</div>
</body>
</html>
```